Simple and Clean business card design

We would like the design to be simple clean and to incorporate our colors.

We are open to your design and talent, we have the dots in our logo as we think of it as data points and we connect data points for people.

We are open to see the great creative and clean design you bring to the table

Contact Information for Business Card

please include: name, position, email, phone and website

Font styles to use
Sans Serif

Requirements
Must have
• my colors incorporated, simplicity
Nice to have
• lots of white space, simplicity
Should not have
• complexicity/ complex art

```html
<!DOCTYPE html>
<html lang="en">
<head>
<meta charset="utf-8">
<title>Dotwise — Business Card</title>
<link rel="stylesheet" href="https://fonts.googleapis.com/css2?family=Open+Sans:wght@400;600&family=Saira+Condensed:wght@700;800&family=Saira:wght@500&display=swap">
<style>
  :root {
    --brand-blue: #4285f4;
    --brand-red: #ea4335;
    --ink: #1f1f1f;
    --paper: #ffffff;
    --page: #fdfdfd;
    --ghost-on-blue: rgba(255, 255, 255, 0.1);
    --ghost-on-white: #e8ecf5;
    --card-edge: #3a3a3a;
  }
  * { box-sizing: border-box; margin: 0; padding: 0; }
  html, body {
    width: 1200px; height: 1200px; overflow: hidden;
    background: var(--page);
    font-family: "Open Sans", sans-serif;
  }
  .sheet { position: relative; width: 1200px; height: 1200px; }

  .card {
    position: absolute; left: 216px; width: 775px; height: 431px; overflow: hidden;
  }

  /* Front */
  .card--front { top: 147px; background: var(--brand-blue); }
  .front__ghost {
    position: absolute; left: 370px; top: 80px;
    font-family: "Open Sans", sans-serif; font-weight: 600;
    font-size: 300px; line-height: 1; color: var(--ghost-on-blue);
    white-space: nowrap;
  }
  .front__brand {
    position: absolute; left: 0; right: 0; top: 0; bottom: 0;
    display: flex; align-items: center; justify-content: center; gap: 14px;
  }
  .front__brand-dot {
    width: 26px; height: 26px; border-radius: 50%; background: var(--paper);
  }
  .front__brand-name {
    font-weight: 600; font-size: 100px; line-height: 1; color: var(--paper);
    letter-spacing: -1px;
  }

  /* Back */
  .card--back {
    top: 631px; background: var(--paper); border: 1px solid var(--card-edge);
  }
  .back__ghost {
    position: absolute; left: 88px; top: 120px;
    font-weight: 600; font-size: 215px; line-height: 1;
    color: var(--ghost-on-white); white-space: nowrap; letter-spacing: -2px;
  }
  .person { position: absolute; left: 44px; top: 52px; }
  .person__name {
    font-family: "Saira Condensed", sans-serif; font-weight: 800;
    font-size: 50px; line-height: 1; letter-spacing: 1px; color: var(--ink);
  }
  .person__first { color: var(--brand-blue); margin-right: 8px; }
  .person__role {
    margin-top: 8px;
    font-family: "Saira", sans-serif; font-weight: 500;
    font-size: 14px; letter-spacing: 1.5px; color: var(--ink);
  }
  .back__brand {
    position: absolute; right: 44px; top: 72px;
    display: flex; align-items: center; gap: 12px;
  }
  .back__brand-dot {
    width: 24px; height: 24px; border-radius: 50%; background: var(--brand-blue);
  }
  .back__brand-name {
    font-weight: 600; font-size: 78px; line-height: 1; color: var(--ink);
    letter-spacing: -1px;
  }
  .divider {
    position: absolute; left: 44px; right: 44px; top: 249px;
    height: 2px; background: var(--brand-blue);
  }
  .contacts {
    position: absolute; left: 44px; top: 270px; list-style: none;
  }
  .contacts__item {
    display: flex; align-items: center; height: 33px;
    font-size: 21px; color: var(--ink);
  }
  .contacts__icon { width: 26px; height: 26px; margin-right: 18px; flex: none; }
  .address {
    position: absolute; right: 44px; top: 270px;
    font-style: normal; text-align: right;
    font-size: 21px; line-height: 33px; color: var(--ink);
  }
  .stripe--red {
    position: absolute; left: 0; right: 0; top: 400px; height: 5px; background: var(--brand-red);
  }
  .stripe--blue {
    position: absolute; left: 0; right: 0; top: 408px; bottom: 0; background: var(--brand-blue);
  }
</style>
</head>
<body>
<main class="sheet">
  <section class="card card--front" aria-label="Card front">
    <div class="front__ghost" aria-hidden="true">Dotwise</div>
    <div class="front__brand">
      <span class="front__brand-dot"></span>
      <span class="front__brand-name">Dotwise</span>
    </div>
  </section>

  <section class="card card--back" aria-label="Card back">
    <div class="back__ghost" aria-hidden="true">Dotwise</div>

    <div class="person">
      <h1 class="person__name"><span class="person__first">OWEN</span>MARSH</h1>
      <p class="person__role">CEO/FOUNDER</p>
    </div>

    <div class="back__brand">
      <span class="back__brand-dot"></span>
      <span class="back__brand-name">Dotwise</span>
    </div>

    <div class="divider"></div>

    <ul class="contacts">
      <li class="contacts__item">
        <svg class="contacts__icon" viewBox="0 0 24 24" aria-hidden="true">
          <path fill="#4285f4" d="M6.6 2.5c.5-.4 1.2-.3 1.5.2l1.3 2c.3.5.2 1.1-.2 1.4l-1 .8c.9 2.8 2.8 5.5 5.3 7.4l1-.8c.4-.3 1-.3 1.4.1l1.8 1.6c.4.4.5 1 .1 1.5l-1.3 1.5c-.8.9-2.1 1.1-3.1.5C8.7 16.5 5.3 12 4.6 7.2c-.2-1.1.3-2.2 1.2-2.9z"/>
        </svg>
        555-014-2290
      </li>
      <li class="contacts__item">
        <svg class="contacts__icon" viewBox="0 0 24 24" aria-hidden="true" fill="none" stroke="#4285f4" stroke-width="1.3">
          <circle cx="12" cy="12" r="10"/>
          <ellipse cx="12" cy="12" rx="4.5" ry="10"/>
          <line x1="12" y1="2" x2="12" y2="22"/>
          <line x1="2" y1="12" x2="22" y2="12"/>
          <path d="M4 7h16M4 17h16"/>
        </svg>
        www.dotwise.io
      </li>
      <li class="contacts__item">
        <svg class="contacts__icon" viewBox="0 0 24 24" aria-hidden="true">
          <rect x="1" y="5" width="22" height="14" fill="#4285f4"/>
          <path d="M1 5l11 8 11-8M1 19l8-7M23 19l-8-7" fill="none" stroke="#fff" stroke-width="1.2"/>
        </svg>
        owen.marsh@dotwise.io
      </li>
    </ul>

    <address class="address">
      Address line goes here<br>
      city name, country name<br>
      ST 00000
    </address>

    <div class="stripe--red"></div>
    <div class="stripe--blue"></div>
  </section>
</main>
</body>
</html>
```